need corporate, modern business card created for Consulting Company

I need a slick business card using elements from my website, as well as, integrating my pixelforge-created logo (see files).

The business card needs to be:
1. Corporate and modern
2. Clean and professional

I've included a PSD with the logo/icon that you can use to create it. Feel free to try a metallic finish on the logo, make it bigger/small, underlay it. Whatever you need to do to make my card stand out.

Try a black background, or white background or gray.

The idea is for my card to be memorable as well as professional and corporate.

Target Market(s)

Corporate business in the US and Canada.

Industry/Entity Type

Business

Contact Information for Business Card

Enterprise Advancing Solutions
Martin Coble, Senior Partner
office: 1 877 555 0143
mobile: 1 519 555 0172
website: http://www.velmorant.com

Requirements
Must have
• Card-related information
• corporate, yet modern
• clean and professional
• incorporate the icon only
• must have an editable form when complete!
Nice to have
• metallic icon might be cool
• try it with white or black

```html
<!DOCTYPE html>
<html lang="en">
<head>
<meta charset="utf-8">
<title>Velmorant business card</title>
<link href="https://fonts.googleapis.com/css2?family=Roboto:wght@400;500&display=swap" rel="stylesheet">
<style>
  :root {
    --stage: #545454;
    --card: #1c1b1b;
    --brand-blue: #2f6bba;
    --text-blue: #3a6fc4;
    --white: #ffffff;
  }
  html, body {
    margin: 0;
    width: 1036px;
    height: 1200px;
    overflow: hidden;
    background: var(--stage);
    font-family: "Roboto", Arial, sans-serif;
  }
  .card {
    position: absolute;
    left: 121px;
    width: 758px;
    height: 438px;
    background: var(--card);
    overflow: hidden;
  }
  .card--front { top: 142px; }
  .card--back { top: 639px; }

  .hero-mark {
    position: absolute;
    left: 20px;
    top: 55px;
    width: 345px;
    height: 345px;
    border-radius: 18px;
    background: var(--brand-blue);
  }
  .wordmark {
    position: absolute;
    margin: 0;
    font-weight: 500;
    color: var(--brand-blue);
    line-height: 1;
    letter-spacing: 0.5px;
  }
  .card--front .wordmark { left: 420px; top: 218px; font-size: 56px; }
  .card--back .wordmark { left: 55px; top: 174px; font-size: 56px; }

  .divider {
    position: absolute;
    width: 2px;
    background: var(--white);
  }
  .divider--top { left: 444px; top: 46px; height: 157px; }
  .divider--bottom { left: 442px; top: 324px; height: 37px; }

  .person {
    position: absolute;
    left: 471px;
    top: 128px;
    margin: 0;
  }
  .person__name {
    display: block;
    color: var(--white);
    font-size: 22px;
    font-weight: 500;
    letter-spacing: 0.3px;
    line-height: 26px;
  }
  .person__role {
    display: block;
    color: var(--text-blue);
    font-size: 21px;
    line-height: 27px;
  }

  .contacts {
    position: absolute;
    left: 430px;
    top: 218px;
    margin: 0;
    padding: 0;
    list-style: none;
  }
  .contacts li {
    display: flex;
    align-items: center;
    height: 36px;
    font-size: 21px;
  }
  .contacts svg { width: 26px; height: 24px; margin-right: 15px; fill: var(--white); }
  .contact--phone { color: var(--text-blue); }
  .contact--web { color: var(--white); }

  .rule {
    position: absolute;
    left: 0;
  }
  .rule--blue { top: 375px; width: 666px; height: 6px; background: var(--brand-blue); }
  .rule--white { top: 395px; width: 663px; height: 5px; background: var(--white); }
</style>
</head>
<body>

<section class="card card--front" aria-label="Card front">
  <div class="hero-mark" aria-hidden="true"></div>
  <p class="wordmark">velmorant</p>
</section>

<section class="card card--back" aria-label="Card back">
  <p class="wordmark">velmorant</p>

  <div class="divider divider--top"></div>
  <div class="divider divider--bottom"></div>

  <p class="person">
    <span class="person__name">MARTIN COBLE</span>
    <span class="person__role">Senior Partner</span>
  </p>

  <ul class="contacts">
    <li class="contact--phone">
      <svg viewBox="0 0 26 24" aria-label="Office phone"><path d="M2 9c0-4 5-6 11-6s11 2 11 6v2h-6V8c-2-1-8-1-10 0v3H2z"/><path d="M6 13h14l3 9H3z M13 15a3 3 0 1 0 0.01 0z" fill-rule="evenodd"/></svg>
      1 877 555 0143
    </li>
    <li class="contact--phone">
      <svg viewBox="0 0 26 24" aria-label="Mobile phone"><path d="M8 0h10a2 2 0 0 1 2 2v20a2 2 0 0 1-2 2H8a2 2 0 0 1-2-2V2a2 2 0 0 1 2-2zm1 3v15h8V3zm4 16.5a1.5 1.5 0 1 0 .01 0z" fill-rule="evenodd"/></svg>
      1 519 555 0172
    </li>
    <li class="contact--web">
      <svg viewBox="0 0 26 24" aria-label="Website"><text x="13" y="19" text-anchor="middle" font-family="Roboto, Arial, sans-serif" font-size="22" font-weight="500" fill="#fff">@</text></svg>
      http://www.velmorant.com
    </li>
  </ul>

  <div class="rule rule--blue"></div>
  <div class="rule rule--white"></div>
</section>

</body>
</html>
```